Tidewell Outfitters Mobile RV Repair

We are looking for a logo and business cards for a new start up business. We will be doing Mobile RV Repair.
We are in Texas.
I don't have any designs at this point.

Contact Information for Business Card

Emphasis should be on the “Mobile RV Repair” and not so much the name “Tidewell Outfitters”

Requirements
Nice to have
• I like the Mobile RV Repair to cover most of the backside of the card! Not sure on the colors, would like to see it in a few different colors!

```html
<!DOCTYPE html>
<html lang="en">
<head>
<meta charset="utf-8">
<title>Tidewell Outfitters Mobile RV Repair – Business Card</title>
<link href="https://fonts.googleapis.com/css2?family=Oswald:wght@500&family=Arimo:wght@400&display=swap" rel="stylesheet">
<style>
  :root {
    --page-bg: #262626;
    --card-bg: #0e0e0e;
    --accent: #e9a81a;
    --text-light: #f2f2f2;
    --text-muted: #d6d6d6;
    --silver: #c4c4c4;
    --divider: #2c2c2c;
  }
  * { margin: 0; padding: 0; box-sizing: border-box; }
  html, body { width: 1200px; height: 900px; overflow: hidden; }
  body {
    background: var(--page-bg);
    display: flex;
    flex-direction: column;
    align-items: center;
    justify-content: center;
    gap: 40px;
    font-family: "Arimo", Arial, sans-serif;
  }
  .card {
    width: 700px;
    height: 400px;
    background: var(--card-bg);
    border-radius: 26px;
    position: relative;
    display: flex;
  }
  /* Brand lockup: one colour, one weight */
  .brand-lockup {
    display: flex;
    flex-direction: column;
    align-items: center;
    gap: 14px;
  }
  .brand-dot {
    width: 60px; height: 60px;
    border-radius: 50%;
    background: var(--accent);
  }
  .brand-name {
    font-family: "Oswald", "Arial Narrow", sans-serif;
    font-weight: 500;
    color: var(--text-light);
    text-transform: uppercase;
    text-align: center;
    line-height: 1;
  }
  .brand-name .company {
    display: block;
    font-size: 16px;
    letter-spacing: 4px;
    margin-bottom: 8px;
  }
  .brand-name .service {
    display: block;
    font-size: 36px;
    letter-spacing: 0.5px;
  }
  /* Front */
  .brand-panel {
    width: 330px;
    display: flex;
    align-items: center;
    justify-content: center;
    border-right: 1px solid var(--divider);
    margin: 40px 0;
  }
  .contact-panel {
    flex: 1;
    padding: 70px 40px 0 50px;
    color: var(--text-muted);
  }
  .person-name {
    font-family: "Oswald", "Arial Narrow", sans-serif;
    font-weight: 500;
    color: var(--accent);
    font-size: 34px;
    text-transform: uppercase;
    line-height: 1;
  }
  .person-role { font-size: 19px; color: var(--text-light); margin-top: 4px; margin-bottom: 22px; }
  .contact-list { list-style: none; }
  .contact-list li {
    display: flex; align-items: center; gap: 10px;
    font-size: 19px; color: var(--text-light); line-height: 1.5;
  }
  .contact-list svg { width: 18px; height: 18px; flex: none; fill: none; stroke: var(--accent); stroke-width: 2; }
  .contact-list .highlight { color: var(--accent); }
  .address { margin-top: 22px; font-size: 19px; line-height: 1.4; color: var(--text-muted); }
  /* Back */
  .card-back { align-items: center; justify-content: center; }
  .card-back .brand-dot { background: var(--silver); width: 50px; height: 50px; }
  .card-back .brand-name { color: var(--silver); }
  .card-back .brand-name .company { font-size: 20px; letter-spacing: 6px; margin-bottom: 12px; }
  .card-back .brand-name .service { font-size: 104px; line-height: 0.98; letter-spacing: 1px; }
</style>
</head>
<body>
  <section class="card card-front">
    <div class="brand-panel">
      <div class="brand-lockup">
        <span class="brand-dot"></span>
        <p class="brand-name"><span class="company">Tidewell Outfitters</span><span class="service">Mobile RV Repair</span></p>
      </div>
    </div>
    <div class="contact-panel">
      <h1 class="person-name">Marcus Hale</h1>
      <p class="person-role">Managing Director</p>
      <ul class="contact-list">
        <li><svg viewBox="0 0 24 24"><path d="M5 3h4l2 5-3 2a12 12 0 0 0 6 6l2-3 5 2v4a2 2 0 0 1-2 2A18 18 0 0 1 3 5a2 2 0 0 1 2-2z"/></svg><span>044-555 018 342</span></li>
        <li><svg viewBox="0 0 24 24"><rect x="2" y="5" width="20" height="14" rx="1"/><path d="M2 6l10 7 10-7"/></svg><span>info@tidewellrv.com</span></li>
        <li><svg viewBox="0 0 24 24"><circle cx="12" cy="12" r="9"/><path d="M3 12h18M12 3c3 3 3 15 0 18M12 3c-3 3-3 15 0 18"/></svg><span>www.<span class="highlight">tidewellrv</span>.com</span></li>
      </ul>
      <p class="address">1180 Pecan Road, Suite 4<br>78701, Texas</p>
    </div>
  </section>
  <section class="card card-back">
    <div class="brand-lockup">
      <span class="brand-dot"></span>
      <p class="brand-name"><span class="company">Tidewell Outfitters</span><span class="service">Mobile RV<br>Repair</span></p>
    </div>
  </section>
</body>
</html>
```